Wealth Advising Business Cards and Stationery
Brightmoor Capital Partners
Wealth Advising Business Cards and Stationery - Financial Services
Creative Brief
Simple
Colin Ashdown
Founder - Managing Director
4419 Hollis Crest Road, Suite 820, Frisco,TX 75036
colin@brightmoorcapitalpartners.example
www.brightmoorcapitalpartners.example
I'd like the logo to be on one side and the contact information on the other.

```html
<!DOCTYPE html>
<html lang="en">
<head>
<meta charset="utf-8">
<title>Brightmoor Capital Partners – Business Card</title>
<link href="https://fonts.googleapis.com/css2?family=Cinzel:wght@400&family=Oswald:wght@300;400&family=Roboto:wght@300&display=swap" rel="stylesheet">
<style>
  :root {
    --backdrop: #1b1b1c;
    --card: #101011;
    --card-edge: #262628;
    --silver: #c9cacc;
    --silver-dim: #9c9da0;
    --rule: #6d6e71;
  }
  * { margin: 0; padding: 0; box-sizing: border-box; }
  html, body {
    width: 1200px; height: 901px; overflow: hidden;
    background: var(--backdrop);
  }
  .canvas {
    width: 1200px; height: 901px;
    display: flex; flex-direction: column;
    align-items: center; justify-content: center; gap: 52px;
  }
  .card {
    width: 620px; height: 354px;
    background: var(--card);
    border: 1px solid var(--card-edge);
    border-radius: 4px;
    position: relative;
  }
  .card-front {
    display: flex; align-items: center; justify-content: center;
  }
  .brand-name {
    font-family: "Cinzel", Georgia, serif;
    font-weight: 400;
    font-size: 30px;
    letter-spacing: 3px;
    color: var(--silver);
    text-transform: uppercase;
  }
  .card-back {
    display: flex; align-items: center;
    padding-left: 44px;
  }
  .identity { width: 196px; }
  .person-name {
    font-family: "Oswald", "Arial Narrow", sans-serif;
    font-weight: 400;
    font-size: 22px;
    letter-spacing: 1px;
    color: var(--silver);
    text-transform: uppercase;
    line-height: 1.1;
  }
  .person-title {
    font-family: "Roboto", Arial, sans-serif;
    font-weight: 300;
    font-size: 12.5px;
    color: var(--silver-dim);
    margin-top: 3px;
  }
  .divider {
    width: 1px; height: 92px;
    background: var(--rule);
    margin: 0 14px 0 4px;
  }
  .contact {
    font-family: "Roboto", Arial, sans-serif;
    font-weight: 300;
    font-size: 12.5px;
    line-height: 17px;
    color: var(--silver);
    list-style: none;
  }
  .contact li { display: flex; align-items: center; gap: 4px; white-space: nowrap; }
  .contact svg { width: 9px; height: 9px; fill: none; stroke: var(--silver); stroke-width: 1.4; flex: none; }
</style>
</head>
<body>
<main class="canvas">
  <section class="card card-front">
    <h1 class="brand-name">Brightmoor Capital Partners</h1>
  </section>

  <section class="card card-back">
    <div class="identity">
      <h2 class="person-name">Colin Ashdown</h2>
      <p class="person-title">Founder - Managing Director</p>
    </div>
    <div class="divider"></div>
    <ul class="contact">
      <li>4419 Hollis Crest Road,</li>
      <li>Suite 820, Frisco,TX 75036</li>
      <li>
        <svg viewBox="0 0 10 10"><path d="M2 1 L4 1 L4.6 3.2 L3.5 4 Q4.5 6 6 6.5 L6.8 5.4 L9 6 L9 8 Q8 9 6.5 8.6 Q2.5 7.4 1.3 3.4 Q1 2 2 1 Z"/></svg>
        2145550182
      </li>
      <li>
        <svg viewBox="0 0 10 10"><rect x="2.5" y="1" width="5" height="8" rx="1"/><line x1="4.3" y1="7.6" x2="5.7" y2="7.6"/></svg>
        2145550247
      </li>
      <li>
        <svg viewBox="0 0 10 10"><rect x="1" y="2.2" width="8" height="5.6"/><path d="M1 2.4 L5 5.4 L9 2.4"/></svg>
        colin@brightmoorcapitalpartners.example
      </li>
      <li>
        <svg viewBox="0 0 10 10"><circle cx="5" cy="5" r="4"/><ellipse cx="5" cy="5" rx="1.8" ry="4"/><line x1="1" y1="5" x2="9" y2="5"/></svg>
        www.brightmoorcapitalpartners.example
      </li>
    </ul>
  </section>
</main>
</body>
</html>
```